Need a business card for my new home staging and redesign business. Business name: Quillamore Interiors. Subtitle: Home styling and staging wizardry

Target Market(s)

Realtors, home sellers

Industry/Entity Type

Real Estate

Contact Information for Business Card

I don't have a website address yet, or a business Facebook account, but would like to include those. Do not have a logo or any graphics

Font styles to use
Sans Serif

Colors

Designer to choose colors to be used in the design.

Requirements
Must have
• Placeholders for contact details, e.g. Phone, email, web address, etc.
Nice to have
• Sophisticated but somewhat whimsical feel. Perhaps a stylized star (or magic wand?) over the "I" in interiors to convey inspiration.
Should not have
• Nothing too cutesy, including cartoon wizards.

```html
<!DOCTYPE html>
<html lang="en">
<head>
<meta charset="utf-8">
<title>Quillamore Interiors – Business Card</title>
<link href="https://fonts.googleapis.com/css2?family=Aldrich&display=swap" rel="stylesheet">
<style>
  :root {
    --page-bg: #e9e6e1;
    --gold: #e3b54a;
    --gold-deep: #c8932c;
    --ink: #1b1c1f;
    --slate: #3a3d42;
    --mist: #6d6f72;
    --text-light: #f4f4f2;
    --text-soft: #c9cacc;
  }
  * { margin: 0; padding: 0; box-sizing: border-box; }
  html, body {
    width: 1200px;
    height: 913px;
    overflow: hidden;
    background: var(--page-bg);
  }
  .canvas {
    position: relative;
    width: 1200px;
    height: 913px;
    display: flex;
    align-items: center;
    justify-content: center;
  }
  .business-card {
    position: relative;
    width: 1000px;
    height: 571px;
    background: linear-gradient(135deg, var(--gold) 0%, var(--gold-deep) 100%);
    box-shadow: 0 18px 40px rgba(0,0,0,0.25);
  }
  .card-face {
    position: absolute;
    inset: 16px;
    overflow: hidden;
  }
  .city-backdrop {
    position: absolute;
    inset: 0;
    background:
      radial-gradient(ellipse at 75% 15%, rgba(150,150,152,0.55) 0%, rgba(150,150,152,0) 55%),
      linear-gradient(160deg, var(--mist) 0%, var(--slate) 40%, var(--ink) 85%);
  }
  .corner-frame {
    position: absolute;
    inset: 0;
    width: 100%;
    height: 100%;
  }
  .corner-frame polygon { fill: var(--gold); }
  .brand {
    position: absolute;
    left: 300px;
    top: 150px;
    display: flex;
    align-items: center;
    gap: 30px;
  }
  .brand-dot {
    width: 34px;
    height: 34px;
    border-radius: 50%;
    background: var(--gold);
    flex: none;
  }
  .brand-name {
    font-family: "Aldrich", sans-serif;
    font-size: 64px;
    line-height: 1.02;
    letter-spacing: 4px;
    color: var(--text-light);
  }
  .tagline {
    position: absolute;
    left: 460px;
    top: 330px;
    font-family: "Aldrich", sans-serif;
    font-size: 19px;
    letter-spacing: 2.5px;
    color: var(--text-light);
  }
  .contact-list {
    position: absolute;
    left: 364px;
    top: 400px;
    width: 540px;
    padding-top: 18px;
    border-top: 2px solid var(--gold);
    display: grid;
    grid-template-columns: 1fr 1fr;
    gap: 14px 24px;
    list-style: none;
    font-family: "Aldrich", sans-serif;
    font-size: 15px;
    letter-spacing: 1px;
    color: var(--text-soft);
  }
  .contact-item {
    display: flex;
    align-items: center;
    gap: 10px;
    white-space: nowrap;
  }
  .contact-label {
    color: var(--gold);
    min-width: 20px;
  }
</style>
</head>
<body>
  <main class="canvas">
    <section class="business-card">
      <div class="card-face">
        <div class="city-backdrop" role="img" aria-label="Misty city skyline photograph in dark grey tones"></div>
        <svg class="corner-frame" viewBox="0 0 968 539" preserveAspectRatio="none" aria-hidden="true">
          <polygon points="720,0 968,0 968,215 940,215 940,28 720,28"/>
          <polygon points="0,300 28,300 28,511 260,511 260,539 0,539"/>
        </svg>
        <div class="brand">
          <span class="brand-dot" aria-hidden="true"></span>
          <h1 class="brand-name">Quillamore<br>Interiors</h1>
        </div>
        <p class="tagline">Home styling and staging wizardry</p>
        <ul class="contact-list">
          <li class="contact-item"><span class="contact-label">T</span>(555) 014-2290</li>
          <li class="contact-item"><span class="contact-label">E</span>hello@quillamore.com</li>
          <li class="contact-item"><span class="contact-label">W</span>www.quillamore.com</li>
          <li class="contact-item"><span class="contact-label">S</span>/quillamoreinteriors</li>
        </ul>
      </div>
    </section>
  </main>
</body>
</html>
```